Travel Group 'Lydgate Group' needs a new business card design

Lydgate Group is a diverse business specialising in bespoke, tailor made holidays to suit all budgets and we are specialists in planning exciting day/short trips to suit all markets. Our target market is very varied going from the corporate client and as well as people in the community who simply want to experience something special.
We are looking for a card design that will encourage people to look at our websites and social media platforms and to see for themselves the different facets to our business. It is essential that the card has social media icons for Folio, Chirp and Snap. We are looking for a card with a blank background with no pictures and for the front side to have the attached Lydgate logo. The card should have similar colour scheme to the attached Lydgate logo.
The card must have the following information on one side:
Maud Penrose
Business Development Manager
maudpenrose@lydgatevoyages.example
Lydgate Group, 87 Quarry Lane
Kilwinning, Ayrshire, Scotland KA19 4TN
+44 (0)1294 730182
And then the card must have the following on the second side:
(Lydgate logo)
(social media icons)
www.lydgatevoyages.example
www.lydgateoutings.example
Target Market(s)
Our target market is very varied going from the corporate client and as well as people in the community who simply want to experience something special.
Industry/Entity Type
Business
Contact Information for Business Card
Maud Penrose
+44 (0)1294 730182
(Lydgate logo)
(social media icons)
www.lydgatevoyages.example
www.lydgateoutings.example
Requirements
Must have
- It is essential that the card has social media icons for Folio, Chirp & Snap.
Should not have
- Should not have any images other than Lydgate logo.

```html
<!DOCTYPE html>
<html lang="en">
<head>
<meta charset="utf-8">
<title>Lydgate Group — Business Card Back</title>
<link rel="stylesheet" href="https://fonts.googleapis.com/css2?family=Cinzel:wght@400;600&display=swap">
<style>
  :root {
    --violet: #6b479b;
    --violet-light: rgba(150, 100, 200, 0.55);
    --magenta: #d83a8b;
    --magenta-deep: #c42f85;
    --magenta-veil: rgba(226, 70, 150, 0.45);
    --navy: #2a2466;
    --brand-dot: #c8178f;
    --white: #ffffff;
    --badge: #6b479b;
  }
  * { margin: 0; padding: 0; box-sizing: border-box; }
  html, body {
    width: 1200px;
    height: 720px;
    overflow: hidden;
    background: var(--violet);
  }
  .card {
    position: relative;
    width: 1200px;
    height: 720px;
    overflow: hidden;
    background: var(--violet);
    font-family: "Cinzel", serif;
  }
  .card__backdrop {
    position: absolute;
    inset: 0;
    width: 1200px;
    height: 720px;
  }
  .brand__mark {
    position: absolute;
    left: 542px;
    top: 104px;
    width: 150px;
    height: 150px;
    border-radius: 50%;
    background: var(--brand-dot);
  }
  .brand {
    position: absolute;
    left: 0;
    top: 286px;
    width: 1200px;
    text-align: center;
    color: var(--navy);
    font-weight: 600;
    font-size: 64px;
    letter-spacing: 7px;
    line-height: 1;
    text-transform: uppercase;
  }
  .social {
    position: absolute;
    top: 521px;
    left: 0;
    width: 1200px;
    height: 68px;
    list-style: none;
  }
  .social__item {
    position: absolute;
    top: 0;
    width: 68px;
    height: 68px;
    border-radius: 50%;
    background: var(--badge);
    display: flex;
    align-items: center;
    justify-content: center;
    color: var(--white);
    font-size: 12px;
    font-weight: 600;
    letter-spacing: 0.5px;
    text-transform: uppercase;
  }
  .social__item--chirp { left: 271px; }
  .social__item--folio { left: 568px; }
  .social__item--snap  { left: 883px; }
  .websites {
    position: absolute;
    left: 0;
    top: 606px;
    width: 1200px;
    text-align: center;
    color: var(--white);
    font-weight: 400;
    font-size: 35px;
    line-height: 43px;
    text-transform: uppercase;
  }
  .websites__link { display: block; }
</style>
</head>
<body>
  <main class="card">
    <svg class="card__backdrop" viewBox="0 0 1200 720" aria-hidden="true">
      <rect width="1200" height="720" fill="var(--violet)"/>
      <path d="M1125 0 L1200 0 L1200 400 L985 440 Q1090 240 1125 0 Z" fill="var(--violet-light)"/>
      <path d="M1180 0 L1200 0 L1200 400 L1030 430 Q1150 230 1180 0 Z" fill="var(--magenta-deep)"/>
      <path d="M0 427 Q560 520 1200 395 L1200 720 L0 720 Z" fill="var(--magenta-veil)"/>
      <path d="M0 466 Q620 525 1200 405 L1200 720 L0 720 Z" fill="var(--magenta)"/>
    </svg>

    <span class="brand__mark" aria-hidden="true"></span>
    <h1 class="brand">Lydgate</h1>

    <ul class="social">
      <li class="social__item social__item--chirp">Chirp</li>
      <li class="social__item social__item--folio">Folio</li>
      <li class="social__item social__item--snap">Snap</li>
    </ul>

    <p class="websites">
      <span class="websites__link">www.lydgatevoyages.example</span>
      <span class="websites__link">www.lydgateoutings.example</span>
    </p>
  </main>
</body>
</html>
```